Health and Wellness company needs flyer to promote free seminar

Corelift studio is a health and wellness company that offers an exercise program designed by physical therapists to help relieve pain and improve mobility. Our business is a new concept that is not well understood by the public. In order to promote our business we offer a free seminar where we present information regarding the underlying cause of pain and tightness. During the seminar we also perform a posture screen and movement testing for all participants.

Target Market(s)

Mostly healthy and active women ages 25-65

Industry/Entity Type

Health And Wellness

Font styles to use
Sans Serif

Colors

Designer to choose colors to be used in the design.

Requirements
Must have
• Title: Eliminate Pain and Tightness For Good
• Paragraph: Corelift Studio offers a free 60 minute seminar: "The Busy Walker's Handbook to Stretching and Standing Taller."
• What to Expect:
• • Identify the underlying cause of your pain and mobility issues
• • Expose what gets in the way of you moving and feeling better
• • Learn why traditional exercises don’t help and can actually make the problem worse
• • Reveal what your posture is saying and how that impacts you
• • Experience your muscle imbalances through movement tests
• • Discover the training method that realigns your posture, increases your mobility and reduces your pain
• Call to action: RSVP online at coreliftstudio.com
Nice to have
• Use a relevant image showing a female dealing with tightness in the low back, legs, etc.
• Emphasize that the seminar is FREE.
• Make the call to action prominent.

```html
<!DOCTYPE html>
<html lang="en">
<head>
<meta charset="utf-8">
<title>Corelift Studio – Free Seminar Flyer</title>
<link rel="stylesheet" href="https://fonts.googleapis.com/css2?family=Bebas+Neue&family=Montserrat:ital,wght@0,400;0,500;0,600;0,700;1,500&display=swap">
<style>
  :root {
    --backdrop: #d6d6d6;
    --paper: #ffffff;
    --purple: #4a4f9c;
    --purple-light: #5a5fb0;
    --orange: #f7931e;
    --orange-deep: #ec8418;
    --ink: #3d3d3d;
    --mist: #e9e9f4;
  }
  * { box-sizing: border-box; margin: 0; padding: 0; }
  html, body {
    width: 1200px; height: 1200px; overflow: hidden;
    background: var(--backdrop);
    font-family: "Montserrat", Arial, sans-serif;
  }
  .flyer {
    position: absolute; left: 152px; top: 20px;
    width: 986px; height: 1276px;
    transform: scale(0.909); transform-origin: top left;
    background: var(--paper);
    overflow: hidden;
    box-shadow: 0 6px 18px rgba(0,0,0,0.25);
  }
  .flyer__shapes { position: absolute; inset: 0; }
  .brand {
    position: absolute; left: 505px; top: 58px;
    display: flex; align-items: center; gap: 16px;
  }
  .brand__square { width: 70px; height: 70px; background: var(--orange); }
  .brand__name { font-size: 44px; font-weight: 700; color: var(--purple); letter-spacing: -1px; }
  .hero-photo { position: absolute; left: 30px; top: 0; width: 440px; height: 615px; }
  .presents {
    position: absolute; left: 460px; width: 430px; top: 244px;
    text-align: center; color: #fff; font-size: 36px; font-style: italic; font-weight: 500;
  }
  .ribbon { position: absolute; left: 462px; top: 305px; width: 420px; height: 72px; }
  .ribbon__label {
    position: absolute; inset: 0; display: flex; align-items: center; justify-content: center;
    color: #fff; font-size: 40px; font-weight: 700;
  }
  .seminar-title {
    position: absolute; left: 486px; width: 394px; top: 398px;
    text-align: center; color: #fff; font-weight: 400;
    font-family: "Bebas Neue", Impact, sans-serif; font-size: 47px; line-height: 57px;
    white-space: nowrap;
  }
  .tagline {
    position: absolute; left: 0; width: 986px; top: 646px;
    text-align: center; color: #fff; font-size: 30px; font-weight: 700;
  }
  .expect { position: absolute; left: 135px; top: 768px; width: 730px; }
  .expect__heading {
    font-family: "Bebas Neue", Impact, sans-serif; font-size: 38px; font-weight: 400; color: var(--purple);
    margin-bottom: 18px;
  }
  .expect__list { list-style: none; }
  .expect__item {
    position: relative; padding-left: 55px;
    font-size: 19.5px; line-height: 32.3px; color: var(--ink);
  }
  .expect__tick { position: absolute; left: 2px; top: 7px; width: 20px; height: 20px; }
  .expect__verb {
    color: var(--orange); font-weight: 700;
    text-decoration: underline; text-underline-offset: 5px; text-decoration-thickness: 1px;
    text-decoration-color: var(--purple);
  }
  .bonus {
    position: absolute; left: 0; width: 986px; top: 1112px;
    display: flex; justify-content: center; align-items: center; gap: 14px;
    font-family: "Bebas Neue", Impact, sans-serif; font-size: 36px; color: var(--purple);
  }
  .bonus__rule { width: 26px; height: 2px; background: var(--orange); }
  .cta {
    position: absolute; left: 0; width: 986px; top: 1219px;
    text-align: center; color: #fff; font-size: 27px; font-weight: 500;
  }
  .cta__url { color: var(--orange); font-weight: 700; }
</style>
</head>
<body>
<main class="flyer">
  <svg class="flyer__shapes" viewBox="0 0 986 1276" width="986" height="1276">
    <path d="M0,40 Q120,0 260,0 C420,150 700,210 986,168 L986,620 C700,650 400,640 0,560 Z" fill="var(--purple)"/>
    <path d="M260,0 C420,150 700,210 986,168 L986,190 C700,232 430,180 300,0 Z" fill="var(--purple-light)" opacity="0.5"/>
    <path d="M0,565 C350,650 700,650 986,605 L986,775 C760,710 560,690 0,755 Z" fill="var(--orange)"/>
    <path d="M0,610 C350,680 700,660 986,650 L986,700 C700,690 350,700 0,640 Z" fill="var(--orange-deep)" opacity="0.5"/>
    <path d="M0,562 C350,645 700,646 986,602" fill="none" stroke="#fff" stroke-width="4"/>
    <path d="M0,1240 C300,1170 650,1175 986,1235" fill="none" stroke="var(--mist)" stroke-width="10"/>
    <path d="M0,1255 C300,1180 650,1180 986,1262 L986,1276 L0,1276 Z" fill="var(--purple)"/>
  </svg>

  <div class="hero-photo" role="img" aria-label="Photo of an active woman from behind in a sports top and shorts, holding her lower back"
       style="background: linear-gradient(180deg, #c98d62 0%, #d9a27a 45%, #e9618f 72%, #ef6c9c 100%);"></div>

  <div class="brand">
    <span class="brand__square"></span>
    <span class="brand__name">corelift studio</span>
  </div>

  <p class="presents">— Presents —</p>

  <div class="ribbon">
    <svg viewBox="0 0 420 72" width="420" height="72">
      <path d="M0,0 H420 L380,36 L420,72 H0 L40,36 Z" fill="var(--orange)"/>
    </svg>
    <span class="ribbon__label">FREE SEMINAR</span>
  </div>

  <h1 class="seminar-title">The Busy Walker's<br>Handbook to Stretching<br>and Standing Taller</h1>

  <p class="tagline">Eliminate Pain and Tightness for Good.</p>

  <section class="expect">
    <h2 class="expect__heading">What to expect:</h2>
    <ul class="expect__list">
      <li class="expect__item"><svg class="expect__tick" viewBox="0 0 20 20"><circle cx="10" cy="10" r="8" fill="none" stroke="var(--purple)" stroke-width="2.2"/><path d="M6,10 L9,13 L14,7" fill="none" stroke="var(--purple)" stroke-width="2.2"/></svg><span class="expect__verb">Identify</span> the underlying cause of your pain and mobility issues</li>
      <li class="expect__item"><svg class="expect__tick" viewBox="0 0 20 20"><circle cx="10" cy="10" r="8" fill="none" stroke="var(--purple)" stroke-width="2.2"/><path d="M6,10 L9,13 L14,7" fill="none" stroke="var(--purple)" stroke-width="2.2"/></svg><span class="expect__verb">Expose</span> what gets in the way of you moving and feeling better</li>
      <li class="expect__item"><svg class="expect__tick" viewBox="0 0 20 20"><circle cx="10" cy="10" r="8" fill="none" stroke="var(--purple)" stroke-width="2.2"/><path d="M6,10 L9,13 L14,7" fill="none" stroke="var(--purple)" stroke-width="2.2"/></svg><span class="expect__verb">Learn</span> why traditional exercises don’t help and can actually make the problem worse</li>
      <li class="expect__item"><svg class="expect__tick" viewBox="0 0 20 20"><circle cx="10" cy="10" r="8" fill="none" stroke="var(--purple)" stroke-width="2.2"/><path d="M6,10 L9,13 L14,7" fill="none" stroke="var(--purple)" stroke-width="2.2"/></svg><span class="expect__verb">Reveal</span> what your posture is saying and how that impacts you</li>
      <li class="expect__item"><svg class="expect__tick" viewBox="0 0 20 20"><circle cx="10" cy="10" r="8" fill="none" stroke="var(--purple)" stroke-width="2.2"/><path d="M6,10 L9,13 L14,7" fill="none" stroke="var(--purple)" stroke-width="2.2"/></svg><span class="expect__verb">Experience</span> your muscle imbalances through movement tests</li>
      <li class="expect__item"><svg class="expect__tick" viewBox="0 0 20 20"><circle cx="10" cy="10" r="8" fill="none" stroke="var(--purple)" stroke-width="2.2"/><path d="M6,10 L9,13 L14,7" fill="none" stroke="var(--purple)" stroke-width="2.2"/></svg><span class="expect__verb">Discover</span> the training method that realigns your posture, increases your mobility and reduces your pain</li>
    </ul>
  </section>

  <p class="bonus"><span class="bonus__rule"></span>Free posture screen &amp; movement testing<span class="bonus__rule"></span></p>

  <p class="cta">RSVP online at <span class="cta__url">coreliftstudio.com</span></p>
</main>
</body>
</html>
```